Letterhead creation for military law attorney

I need letterhead design for my business. We are now only doing military law and need to change address, logo and vision. I like the idea of using an eagle or a jolly roger flag

Target Market(s)

Military Law Clients

Colors
3176b5
85abd2

Requirements
Must have
• We are defending people against the government
Nice to have
• Jolly Roger Flag

```html
<!DOCTYPE html>
<html lang="en">
<head>
<meta charset="utf-8">
<title>Harlow Defense, PLLC — Stationery</title>
<link href="https://fonts.googleapis.com/css2?family=Cinzel:wght@500&family=Open+Sans:wght@600&display=swap" rel="stylesheet">
<style>
  :root{
    --brand-blue:#84a9d4;
    --brand-deep:#3176b5;
    --ink:#231f20;
    --paper:#ffffff;
    --backdrop:#e4e5e7;
    --text-dark:#1d1d1d;
  }
  *{margin:0;padding:0;box-sizing:border-box}
  html,body{width:1200px;height:1200px;overflow:hidden;background:var(--backdrop)}
  .canvas{position:relative;width:1200px;height:1200px}

  .wordmark{font-family:"Cinzel",serif;font-weight:500;text-align:center;line-height:1}
  .wordmark .name{display:block;letter-spacing:.02em}
  .wordmark .suffix{display:block;letter-spacing:.04em}
  .mark-dot{display:block;margin:0 auto;border-radius:50%}

  /* Letterhead */
  .letterhead{position:absolute;left:384px;top:104px;width:690px;height:976px;background:var(--paper);box-shadow:0 4px 14px rgba(0,0,0,.18)}
  .letterhead-header{position:absolute;left:0;top:0;width:690px;height:125px}
  .letterhead .wordmark{position:absolute;left:40px;top:36px;width:160px;color:var(--paper)}
  .letterhead .mark-dot{width:26px;height:26px;background:var(--paper);margin-bottom:8px}
  .letterhead .name{font-size:14px}
  .letterhead .suffix{font-size:7px;margin-top:3px}
  .contact{position:absolute;right:39px;top:53px;font-family:"Open Sans",sans-serif;font-weight:600;font-size:10.5px;color:var(--text-dark);text-align:right;line-height:14px}
  .contact .row{display:flex;justify-content:flex-end;align-items:center;gap:3px}
  .contact .gap{margin-top:5px}
  .contact svg{width:10px;height:10px;fill:var(--brand-blue)}
  .letterhead-footer{position:absolute;left:0;bottom:0;width:690px;height:54px}
  .social{position:absolute;left:72px;bottom:15px;display:flex;gap:12px}
  .social span{width:20px;height:20px;border-radius:50%;background:var(--paper)}
  .email{position:absolute;right:39px;bottom:20px;font-family:"Open Sans",sans-serif;font-weight:600;font-size:10.5px;color:var(--text-dark);display:flex;align-items:center;gap:4px}
  .email svg{width:10px;height:8px;fill:var(--paper)}

  /* Card back (blue) */
  .card-back{position:absolute;left:116px;top:538px;width:521px;height:442px;background:var(--brand-blue);box-shadow:8px 10px 18px rgba(0,0,0,.2)}
  .card-back .wordmark{position:absolute;left:0;right:0;top:120px;color:var(--paper)}
  .card-back .mark-dot{width:110px;height:110px;background:var(--paper);margin-bottom:26px}
  .card-back .name{font-size:34px}
  .card-back .suffix{font-size:16px;margin-top:6px}

  /* Card front (dark) */
  .card-front{position:absolute;left:53px;top:365px;width:280px;height:238px;background:var(--ink);box-shadow:6px 8px 14px rgba(0,0,0,.25)}
  .card-front .wordmark{position:absolute;left:0;right:0;top:60px;color:var(--paper)}
  .card-front .mark-dot{width:56px;height:56px;background:var(--brand-blue);margin-bottom:16px}
  .card-front .name{font-size:18px}
  .card-front .suffix{font-size:9px;margin-top:4px;color:var(--brand-blue)}
</style>
</head>
<body>
<main class="canvas">

  <section class="letterhead" aria-label="Letterhead">
    <svg class="letterhead-header" viewBox="0 0 690 125" aria-hidden="true">
      <path d="M0 0H690V38H304L256 125H0Z" fill="var(--brand-blue)"/>
    </svg>
    <div class="wordmark">
      <span class="mark-dot"></span>
      <span class="name">HARLOW</span>
      <span class="suffix">DEFENSE, PLLC</span>
    </div>
    <address class="contact" style="font-style:normal">
      <div class="row"><svg viewBox="0 0 10 10"><path d="M5 0a3.5 3.5 0 0 0-3.5 3.5C1.5 6 5 10 5 10s3.5-4 3.5-6.5A3.5 3.5 0 0 0 5 0zm0 5a1.5 1.5 0 1 1 0-3 1.5 1.5 0 0 1 0 3z"/></svg>: 2045 CANYON RIDGE RD #310</div>
      <div class="row">BOULDER CITY , NV 89005</div>
      <div class="row gap"><svg viewBox="0 0 10 10"><path d="M2 0l2 2.5-1 1.2a6 6 0 0 0 3.3 3.3l1.2-1L10 8 8.5 10C4 10 0 6 0 1.5z"/></svg>: (555) 014-2200</div>
      <div class="row"><svg viewBox="0 0 10 10"><path d="M2 0h5v3H2zM0 3.5h10v4H8V10H2V7.5H0zM3 6v3h4V6z"/></svg>: (555) 014-2201</div>
      <div class="row"><svg viewBox="0 0 10 10"><path d="M2.5 0h5v10h-5zM3.3 1v7.5h3.4V1z"/></svg>: (555) 014-3390</div>
    </address>
    <svg class="letterhead-footer" viewBox="0 0 690 54" aria-hidden="true">
      <rect x="0" y="0" width="240" height="54" fill="var(--ink)"/>
      <path d="M240 0H690V54H240L216 27Z" fill="var(--paper)"/>
      <path d="M250 0H690V54H250L228 27Z" fill="var(--brand-blue)"/>
      <path d="M216 27L240 0H232L210 27 232 54H240Z" fill="var(--ink)"/>
    </svg>
    <div class="social" aria-label="Social links"><span></span><span></span><span></span></div>
    <div class="email"><svg viewBox="0 0 10 8"><path d="M0 0h10v8H0zM1 1l4 3 4-3z"/></svg>: office@harlowdefense.com</div>
  </section>

  <section class="card-back" aria-label="Business card back">
    <div class="wordmark">
      <span class="mark-dot"></span>
      <span class="name">HARLOW</span>
      <span class="suffix">DEFENSE, PLLC</span>
    </div>
  </section>

  <section class="card-front" aria-label="Business card front">
    <div class="wordmark">
      <span class="mark-dot"></span>
      <span class="name">HARLOW</span>
      <span class="suffix">DEFENSE, PLLC</span>
    </div>
  </section>

</main>
</body>
</html>
```